Small rum distillery looking for bottle design

Small rum distillery in Estonia. Looking for bottle lable design. It should be simple but at the same time point out from the variety of other bottles.
As we are a small nordic country, design can be some how nordic or represent our country. It can also have some connection with sailing or sea as we know it pirates love it.
Bottle we are using is Corvane 540

Industry/Entity Type

food and beverage

Other font styles liked:
• Baskerville

```html
<!DOCTYPE html>
<html lang="en">
<head>
<meta charset="utf-8">
<title>Halde Distillery – Rum Label</title>
<link rel="stylesheet" href="https://fonts.googleapis.com/css2?family=EB+Garamond:ital,wght@0,400;0,500;1,400&display=swap">
<style>
  :root {
    --backdrop: #3f3e40;
    --label-paper: #e1e2d4;
    --wheel-tint: #ecece3;
    --ink-grey: #58585a;
    --ink-red: #b9302e;
  }
  html, body {
    margin: 0;
    padding: 0;
    width: 1200px;
    height: 1200px;
    overflow: hidden;
    background: var(--backdrop);
  }
  .canvas {
    position: relative;
    width: 1200px;
    height: 1200px;
  }
  .rum-label {
    position: absolute;
    left: 390px;
    top: 390px;
    width: 420px;
    height: 420px;
  }
  .label-paper { fill: var(--label-paper); }
  .wheel-area { fill: var(--wheel-tint); }
  .brand-mark { fill: none; stroke: var(--ink-grey); stroke-width: 2; }
  .label-text { font-family: "EB Garamond", Baskerville, serif; }
  .spirit-type { fill: var(--ink-red); font-style: italic; font-size: 27px; letter-spacing: 9px; }
  .brand-name { fill: var(--ink-grey); font-size: 56px; font-weight: 500; letter-spacing: 1px; }
  .brand-rule { stroke: var(--ink-grey); stroke-width: 2; }
  .brand-sub { fill: var(--ink-grey); font-size: 18px; letter-spacing: 5px; }
  .volume { fill: var(--ink-red); font-size: 20px; }
  .strength { fill: var(--ink-grey); font-size: 19px; }
  .strength-note { fill: var(--ink-grey); font-size: 8.5px; }
</style>
</head>
<body>
<main class="canvas">
  <svg class="rum-label" viewBox="0 0 420 420" xmlns="http://www.w3.org/2000/svg">
    <defs>
      <path id="petal-quadrant" d="M210,210 L210,0 C235,22 285,38 315,58 C345,78 345,100 320,100 C320,75 342,75 362,105 C382,135 398,185 420,210 Z"/>
    </defs>
    <g class="label-paper">
      <use href="#petal-quadrant"/>
      <use href="#petal-quadrant" transform="rotate(90 210 210)"/>
      <use href="#petal-quadrant" transform="rotate(180 210 210)"/>
      <use href="#petal-quadrant" transform="rotate(270 210 210)"/>
      <circle cx="210" cy="210" r="40"/>
    </g>

    <circle class="wheel-area" cx="210" cy="195" r="108" role="img" aria-label="Faint ship's wheel illustration behind the label text"/>

    <g class="label-text" text-anchor="middle">
      <text class="spirit-type" x="214" y="86">rum</text>
      <circle class="brand-mark" cx="210" cy="150" r="14"/>
      <text class="brand-name" x="210" y="248">HALDE</text>
      <line class="brand-rule" x1="95" y1="261" x2="325" y2="261"/>
      <text class="brand-sub" x="212" y="287">DISTILLERY</text>
      <text class="volume" x="210" y="334">700ml</text>
      <text class="strength" x="210" y="366">40%</text>
      <text class="strength-note" x="210" y="378">alc. by vol.</text>
    </g>
  </svg>
</main>
</body>
</html>
```